Copper lark buildworks

Copper lark buildworks is a small construction company.
Who is a licenced builder, Carpenter, joiner,
working on heritage ,new build, speacial projects and sometimes furniture

Industry/Entity Type

Construction

```html
<!DOCTYPE html>
<html lang="en">
<head>
<meta charset="utf-8">
<title>Copper lark buildworks – Business Card</title>
<link rel="stylesheet" href="https://fonts.googleapis.com/css2?family=Baloo+2:wght@700&family=Quicksand:wght@600&family=Open+Sans:ital,wght@0,300;0,400;1,400&display=swap">
<style>
  :root {
    --charcoal: #3c3c3e;
    --teal: #1ca89c;
    --white: #ffffff;
    --page: #eef0ef;
    --ink: #2b2b2b;
  }
  * { box-sizing: border-box; margin: 0; padding: 0; }
  html, body {
    width: 1200px;
    height: 1200px;
    overflow: hidden;
    background: var(--page);
  }
  .card {
    position: absolute;
    left: 80px;
    top: 303px;
    width: 1040px;
    height: 594px;
    background: var(--teal);
    box-shadow: 0 10px 30px rgba(0,0,0,0.18);
    overflow: hidden;
  }
  .header-band {
    position: absolute;
    left: 0; top: 0;
    width: 100%;
    height: 159px;
    background: var(--charcoal);
    display: flex;
    align-items: center;
    justify-content: center;
  }
  .company-name {
    font-family: "Baloo 2", sans-serif;
    font-weight: 700;
    font-size: 48px;
    color: var(--teal);
    letter-spacing: 0.5px;
    padding-top: 8px;
    padding-left: 40px;
  }
  .accent-strip {
    position: absolute;
    left: 0; top: 159px;
    width: 100%;
    height: 45px;
    background: var(--teal);
  }
  .identity-band {
    position: absolute;
    left: 0; top: 204px;
    width: 100%;
    height: 139px;
    background: var(--white);
  }
  .notch {
    position: absolute;
    left: 484px;
    top: 204px;
    width: 76px;
    height: 30px;
  }
  .person-name {
    position: absolute;
    left: 150px;
    top: 225px;
    font-family: "Quicksand", sans-serif;
    font-weight: 600;
    font-size: 45px;
    color: var(--teal);
  }
  .person-role {
    position: absolute;
    left: 367px;
    top: 286px;
    font-family: "Open Sans", sans-serif;
    font-style: italic;
    font-size: 23px;
    color: var(--ink);
  }
  .phone {
    position: absolute;
    left: 583px;
    top: 250px;
    display: flex;
    align-items: center;
    gap: 24px;
  }
  .phone-icon { width: 24px; height: 40px; }
  .phone-number {
    font-family: "Open Sans", sans-serif;
    font-weight: 300;
    font-size: 42px;
    color: var(--teal);
    letter-spacing: 1px;
  }
  .services {
    position: absolute;
    left: 0; top: 343px;
    width: 100%;
    height: 251px;
    font-family: "Open Sans", sans-serif;
    font-size: 23px;
    color: var(--white);
  }
  .service-col {
    position: absolute;
    top: 60px;
    list-style: none;
  }
  .service-col li { height: 51px; line-height: 30px; }
  .col-one { left: 57px; }
  .col-two { left: 371px; }
  .col-three { left: 740px; }
  .service-heading { padding-left: 0; }
  .service-item { padding-left: 3px; }
</style>
</head>
<body>
  <article class="card">
    <header class="header-band">
      <h1 class="company-name">Copper lark buildworks</h1>
    </header>
    <div class="accent-strip"></div>
    <section class="identity-band"></section>
    <svg class="notch" viewBox="0 0 76 30" aria-hidden="true">
      <polygon points="0,0 76,0 38,30" fill="var(--teal)"/>
    </svg>

    <h2 class="person-name">Tobin Hale</h2>
    <p class="person-role">Owner</p>

    <div class="phone">
      <svg class="phone-icon" viewBox="0 0 24 40" aria-hidden="true">
        <rect x="2" y="2" width="20" height="36" rx="4" fill="none" stroke="var(--teal)" stroke-width="2.5"/>
        <line x1="2" y1="9" x2="22" y2="9" stroke="var(--teal)" stroke-width="2"/>
        <line x1="2" y1="30" x2="22" y2="30" stroke="var(--teal)" stroke-width="2"/>
        <circle cx="12" cy="34" r="1.6" fill="var(--teal)"/>
      </svg>
      <span class="phone-number">0491570156</span>
    </div>

    <section class="services">
      <ul class="service-col col-one">
        <li class="service-heading">Services</li>
        <li class="service-item">- Licensed builder</li>
        <li class="service-item">- Carpenter</li>
      </ul>
      <ul class="service-col col-two">
        <li class="service-item">- Joiner</li>
        <li class="service-item">- New Build</li>
        <li class="service-item">- Special Projects</li>
      </ul>
      <ul class="service-col col-three">
        <li>&nbsp;</li>
        <li class="service-item">- Furniture</li>
        <li class="service-item">- Working On Heritage</li>
      </ul>
    </section>
  </article>
</body>
</html>
```